Adventure Business Cards

Please check out our website for style
Vertical card
Details:
Side 1
Logo
Business name: Kestrel Point Wildland Tours
Name: Colin Warbeck
Role: Director
Email: info@kestrelpointtours.com
Address: PO Box 71, Marlin Cove NSW 2471
Phone: +61 2 5550 1847
Web address: www.kestrelpointtours.com
Side 2
Taking pictures?
A Friendwall and Pixlane logo
Tag us in your pictures with
#kpwildtours
@kpwildtours
www.kestrelpointtours.com
Details:
Side 1
Logo
Name: Colin Warbeck
Role: Director
Phone: +61 2 5550 1847
Side 2
Taking pictures?
#kpwildtours
@kpwildtours

```html
<!DOCTYPE html>
<html lang="en">
<head>
<meta charset="utf-8">
<title>Kestrel Point Wildland Tours – Business Cards</title>
<link href="https://fonts.googleapis.com/css2?family=Open+Sans:wght@400;600;700&display=swap" rel="stylesheet">
<style>
  :root {
    --backdrop: #4a4541;
    --card-white: #ffffff;
    --card-back: #f1f1f1;
    --ink: #111111;
    --photo-light: #e4e4e4;
    --photo-mid: #c9c9c9;
    --photo-dark: #a9a9a9;
  }
  * { margin: 0; padding: 0; box-sizing: border-box; }
  html, body {
    width: 1200px; height: 1000px; overflow: hidden;
    background: var(--backdrop);
    font-family: "Open Sans", Arial, sans-serif;
    color: var(--ink);
  }
  .canvas { position: relative; width: 1200px; height: 1000px; }
  .card {
    position: absolute; top: 170px; width: 398px; height: 665px;
    border-radius: 199px 199px 18px 18px / 165px 165px 18px 18px;
    overflow: hidden; text-align: center;
  }
  .card--back { left: 170px; background: var(--card-back); }
  .card--front { left: 629px; background: var(--card-white); }
  .line { position: absolute; left: 0; right: 0; }

  .back-photo {
    position: absolute; inset: 0;
    background: radial-gradient(ellipse at 50% 45%, var(--photo-mid) 0%, var(--photo-light) 55%, var(--card-back) 100%);
    opacity: .8;
  }
  .back-title { top: 118px; font-size: 33px; font-weight: 600; }
  .back-tag { top: 368px; font-size: 18px; }
  .back-tag b { font-weight: 700; }
  .back-handles { top: 405px; font-size: 18px; }
  .social-row {
    top: 445px; display: flex; justify-content: center; align-items: center;
    gap: 12px; font-size: 16px;
  }
  .social-dot { width: 28px; height: 28px; border-radius: 50%; background: var(--ink); }
  .social-gap { width: 14px; }
  .back-web { top: 572px; font-size: 16px; }
  .back-web b { font-weight: 700; }

  .brand-mark {
    position: absolute; top: 38px; left: 53px; width: 292px; height: 292px;
    border-radius: 50%; background: var(--ink);
    display: flex; align-items: center; justify-content: center;
  }
  .brand-name {
    color: var(--card-white); font-size: 30px; font-weight: 700; line-height: 1.2;
    width: 220px;
  }
  .person-name { top: 386px; font-size: 28px; font-weight: 600; }
  .person-role { top: 421px; font-size: 15px; }
  .contact-icons { position: absolute; top: 474px; left: 92px; }
  .contact-text { font-size: 16px; }
  .contact-address { top: 522px; }
  .contact-phone { top: 556px; }
  .contact-email { top: 581px; }
  .contact-web { top: 606px; }
</style>
</head>
<body>
<div class="canvas">

  <section class="card card--back">
    <div class="back-photo" role="img" aria-label="Faded black and white photo of a person holding a camera up to their face"></div>
    <h2 class="line back-title">Taking pictures?</h2>
    <p class="line back-tag"><b>Tag</b> us in your <b>pictures</b> with</p>
    <p class="line back-handles">#kpwildtours &nbsp;| @kpwildtours</p>
    <div class="line social-row">
      <span>Pixlane</span><span class="social-dot"></span>
      <span class="social-gap"></span>
      <span class="social-dot"></span><span>Friendwall</span>
    </div>
    <p class="line back-web">www.<b>kestrelpointtours</b>.com</p>
  </section>

  <section class="card card--front">
    <div class="brand-mark">
      <span class="brand-name">Kestrel Point Wildland Tours</span>
    </div>
    <h1 class="line person-name">Colin Warbeck</h1>
    <p class="line person-role">Director</p>

    <svg class="contact-icons" width="214" height="32" viewBox="0 0 214 32" aria-hidden="true">
      <line x1="0" y1="16" x2="214" y2="16" stroke="#111" stroke-width="2"/>
      <g fill="#111">
        <circle cx="44" cy="16" r="14"/>
        <circle cx="86" cy="16" r="14"/>
        <circle cx="128" cy="16" r="14"/>
        <circle cx="170" cy="16" r="14"/>
      </g>
      <g fill="#fff" stroke="#fff">
        <path d="M44 25 C39 18 38 16 38 13 a6 6 0 0 1 12 0 c0 3 -1 5 -6 12z" stroke="none"/>
        <circle cx="44" cy="13" r="2" fill="#111" stroke="none"/>
        <path d="M79 12 q7 -5 14 0 l-2 3 h-10z" stroke="none"/>
        <rect x="80" y="15" width="12" height="7" rx="1" stroke="none"/>
        <rect x="121" y="11" width="14" height="10" fill="none" stroke-width="1.6"/>
        <polyline points="121,11 128,17 135,11" fill="none" stroke-width="1.6"/>
        <circle cx="170" cy="16" r="7" fill="none" stroke-width="1.6"/>
        <line x1="163" y1="16" x2="177" y2="16" stroke-width="1.4"/>
        <ellipse cx="170" cy="16" rx="3" ry="7" fill="none" stroke-width="1.4"/>
      </g>
    </svg>

    <p class="line contact-text contact-address">PO Box 71, Marlin Cove NSW 2471</p>
    <p class="line contact-text contact-phone">+61 2 5550 1847</p>
    <p class="line contact-text contact-email">info@kestrelpointtours.com</p>
    <p class="line contact-text contact-web">www.kestrelpointtours.com</p>
  </section>

</div>
</body>
</html>
```